Holvik Cabinets Quality Custom Built Kitchens, Vanity Units, Robes ect

Hi,
Was after a new design for our business cards,
we are a cabinet making business and pride ourselves in quality custom built Kitchens, Vanity units, robes ect.
we have been around for over 20 years and we are trying to modernize our card logo.
Looking for something eye catching, bold and exciting
family ran and operated business, we work with builders and also have a large private clientel.

Thanks

Industry/Entity Type

Business

Contact Information for Business Card

Holvik Cabinets

Font styles to use
Serif
Script

Requirements
Must have
• Corinne 0461735928 hvcabinets@mailvane.com
• Po Box 2786
• 5B Wattlebark Court Kelsbrook Vic 3917
• Phone (03)59286417 Fax (03) 59286942
Nice to have
• Quality Custom Built Kitchens & Vanity Units

```html
<!DOCTYPE html>
<html lang="en">
<head>
<meta charset="utf-8">
<title>Holvik Cabinets – Business Card</title>
<link rel="stylesheet" href="https://fonts.googleapis.com/css2?family=Fira+Sans:wght@300;400;700&display=swap">
<style>
  :root {
    --card-bg: #4a4a4a;
    --card-bg-light: #515151;
    --ink: #ffffff;
    --ink-soft: #f0f0f0;
  }
  html, body {
    margin: 0;
    padding: 0;
    width: 1200px;
    height: 704px;
    overflow: hidden;
    background: var(--card-bg);
  }
  .card {
    position: relative;
    width: 1200px;
    height: 704px;
    overflow: hidden;
    font-family: "Fira Sans", Arial, sans-serif;
    color: var(--ink);
  }
  .card__texture {
    position: absolute;
    inset: 0;
    background: linear-gradient(180deg, var(--card-bg-light) 0%, var(--card-bg) 100%);
  }
  .brand {
    position: absolute;
    left: 102px;
    top: 100px;
    margin: 0;
    font-weight: 700;
    font-size: 92px;
    line-height: 74px;
    letter-spacing: -1.5px;
    text-transform: uppercase;
  }
  .contact-person {
    position: absolute;
    left: 101px;
    top: 392px;
    margin: 0;
    font-weight: 300;
  }
  .contact-person__name {
    font-size: 44px;
    text-transform: uppercase;
    letter-spacing: -0.5px;
  }
  .contact-person__mobile {
    font-size: 32px;
    margin-left: 18px;
  }
  .contact-person__email {
    display: block;
    font-size: 30px;
    margin-top: 4px;
  }
  .office {
    position: absolute;
    left: 527px;
    top: 484px;
    margin: 0;
    font-weight: 300;
    font-size: 29px;
    line-height: 45px;
    font-style: normal;
    color: var(--ink-soft);
  }
  .office__line { display: block; white-space: nowrap; }
  .office__fax { position: absolute; left: 333px; }
</style>
</head>
<body>
  <main class="card">
    <div class="card__texture" role="img" aria-label="Dark grey background with fine wavy line texture"></div>

    <h1 class="brand">Holvik<br>Cabinets</h1>

    <p class="contact-person">
      <span class="contact-person__name">Corinne</span><span class="contact-person__mobile">0461735928</span>
      <span class="contact-person__email">hvcabinets@mailvane.com</span>
    </p>

    <address class="office">
      <span class="office__line">5B Wattlebark Court Kelsbrook Vic 3917</span>
      <span class="office__line">Po Box 2786</span>
      <span class="office__line">Phone (03)59286417<span class="office__fax">Fax (03) 59286942</span></span>
    </address>
  </main>
</body>
</html>
```